Brookvale Harbour Clinic advertising

I have a copy that we had done several years ago. I loved it and still do. Unfortunately, the original graphic designer lost the original artwork. What I do have is the same artwork at a small fridge magnet size. I need to new artwork to look like the small magnet version.
The main brief is to appeal to our clients who have addiction problems. It needs to be edgy and as far removed from the typical medical center images

Requirements
Must have
• The print quality must be able to be blown up to 1m x 2m.

```html
<!DOCTYPE html>
<html lang="en">
<head>
<meta charset="utf-8">
<title>Brookvale Harbour Clinic – Heroin Treatment Billboard</title>
<link rel="stylesheet" href="https://fonts.googleapis.com/css2?family=Fira+Sans+Condensed:wght@400;500&family=Open+Sans:wght@700&display=swap">
<style>
  :root {
    --page-bg: #e4e4e4;
    --board-black: #0a0809;
    --text-white: #ffffff;
    --text-teal: #86a99f;
    --skin-highlight: #c9b0a0;
    --skin-light: #a88b78;
    --skin-mid: #7d6252;
    --skin-dark: #3a2b24;
    --shadow-deep: #1a1311;
  }
  * { margin: 0; padding: 0; box-sizing: border-box; }
  html, body {
    width: 1200px;
    height: 1200px;
    overflow: hidden;
    background: var(--page-bg);
  }
  .billboard {
    position: absolute;
    left: 0;
    top: 300px;
    width: 1200px;
    height: 600px;
    background: var(--board-black);
    overflow: hidden;
  }
  .billboard__photo {
    position: absolute;
    left: 0;
    top: 0;
    width: 1200px;
    height: 600px;
  }
  .billboard__copy {
    position: absolute;
    left: 44px;
    top: 0;
    font-family: "Fira Sans Condensed", "Arial Narrow", sans-serif;
    color: var(--text-white);
  }
  .headline {
    position: absolute;
    top: 44px;
    left: 0;
    font-family: "Open Sans", Arial, sans-serif;
    font-weight: 700;
    font-size: 80px;
    letter-spacing: 5px;
    line-height: 1;
    white-space: nowrap;
  }
  .tagline {
    position: absolute;
    top: 140px;
    left: 0;
    font-weight: 500;
    font-size: 43px;
    line-height: 49px;
    white-space: nowrap;
  }
  .contact {
    position: absolute;
    top: 352px;
    left: 0;
    white-space: nowrap;
  }
  .contact__phone {
    font-family: "Open Sans", Arial, sans-serif;
    font-weight: 700;
    font-size: 49px;
    letter-spacing: 3px;
    color: var(--text-teal);
    line-height: 60px;
  }
  .contact__line {
    font-size: 36px;
    line-height: 49px;
    letter-spacing: 1px;
  }
  .contact__clinic,
  .contact__web { color: var(--text-teal); }
  .contact__offer { color: var(--text-white); font-weight: 500; }
</style>
</head>
<body>
  <section class="billboard">
    <svg class="billboard__photo" viewBox="0 0 1200 600" role="img" aria-label="Close-up portrait photograph with cracked, dry skin texture and green eyes, fading into black on the left">
      <defs>
        <linearGradient id="skinSweep" x1="0" x2="1" y1="0" y2="0">
          <stop offset="0" stop-color="var(--board-black)"/>
          <stop offset="0.36" stop-color="var(--board-black)"/>
          <stop offset="0.46" stop-color="var(--shadow-deep)"/>
          <stop offset="0.56" stop-color="var(--skin-mid)"/>
          <stop offset="0.72" stop-color="var(--skin-light)"/>
          <stop offset="0.86" stop-color="var(--skin-mid)"/>
          <stop offset="0.94" stop-color="var(--skin-dark)"/>
          <stop offset="1" stop-color="var(--shadow-deep)"/>
        </linearGradient>
        <radialGradient id="skinGlow" cx="0.66" cy="0.6" r="0.3">
          <stop offset="0" stop-color="var(--skin-highlight)" stop-opacity="0.7"/>
          <stop offset="1" stop-color="var(--skin-highlight)" stop-opacity="0"/>
        </radialGradient>
        <linearGradient id="edgeShade" x1="0" x2="0" y1="0" y2="1">
          <stop offset="0" stop-color="var(--shadow-deep)" stop-opacity="0.25"/>
          <stop offset="0.25" stop-color="var(--shadow-deep)" stop-opacity="0"/>
          <stop offset="0.85" stop-color="var(--shadow-deep)" stop-opacity="0"/>
          <stop offset="1" stop-color="var(--shadow-deep)" stop-opacity="0.3"/>
        </linearGradient>
      </defs>
      <rect x="0" y="0" width="1200" height="600" fill="url(#skinSweep)"/>
      <rect x="0" y="0" width="1200" height="600" fill="url(#skinGlow)"/>
      <rect x="480" y="0" width="720" height="600" fill="url(#edgeShade)"/>
    </svg>

    <div class="billboard__copy">
      <h1 class="headline">HEROIN</h1>
      <p class="tagline">Got a problem?<br>We Can Help.</p>
      <div class="contact">
        <p class="contact__phone">02555 01846</p>
        <p class="contact__line contact__clinic">Brookvale Harbour Clinic</p>
        <p class="contact__line contact__offer">Free Treatment Available</p>
        <p class="contact__line contact__web">www.brookvaleharbour.com.au</p>
      </div>
    </div>
  </section>
</body>
</html>
```